Insurance Agency website design for Halvern Crest Insurance, LP

Build a website for Halvern Crest Insurance, LP which sells Homeowners, Auto, Renters, Condo, Flood, Disability, Life, Umbrella, and health insurance. We need the coolest insurance agency website out there to get quotes, contact us, or get additional information. Please list the following insurance companies we work with: Dravo, Velk, Meridale Union, Tarvix, Brookwynd, QZT, and Pellurian.

Target Market(s)

Make a design similar to https://www.fandelmora.example/

Industry/Entity Type

Selling personal insurance policies

Coding

Coded - Design and coding required

Number of Pages Required

3 page

```html
<!DOCTYPE html>
<html lang="en">
<head>
<meta charset="utf-8">
<title>Halvern Crest Insurance, LP</title>
<link href="https://fonts.googleapis.com/css2?family=Lexend:wght@400;500;600&family=Montserrat:wght@400;500;600;700&display=swap" rel="stylesheet">
<style>
:root{
  --navy:#1b3f8e;
  --navy-deep:#143780;
  --blue:#1976d2;
  --sky:#2a9be0;
  --green:#7cb342;
  --green-dark:#6aa332;
  --ink:#2b2f3a;
  --muted:#4a5160;
  --light:#f2f4f8;
  --line:#d7deea;
  --white:#fff;
}
*{box-sizing:border-box;margin:0;padding:0}
html,body{width:1200px;height:4332px;overflow:hidden}
body{font-family:'Montserrat',sans-serif;color:var(--ink);background:var(--white);position:relative}
.abs{position:absolute}
h1,h2,h3,.head{font-family:'Lexend',sans-serif;font-weight:500}
.btn{position:absolute;display:flex;align-items:center;justify-content:center;gap:8px;border-radius:40px;font-weight:700;color:var(--white);font-size:13px;letter-spacing:.3px}
.btn-green{background:var(--green)}
.btn-navy{background:var(--navy-deep)}
.chev{width:8px;height:12px}
.brand{display:flex;align-items:center;gap:10px}
.brand-mark{width:30px;height:30px;border:3px solid var(--blue);border-radius:4px;flex:none}
.brand-name{font-family:'Lexend',sans-serif;font-weight:500;color:var(--navy);font-size:17px;line-height:19px;text-transform:uppercase}
.ph{position:absolute}
.eyebrow{font-size:14px;letter-spacing:2px;color:var(--green);font-weight:500}
.underline{position:absolute;height:4px;border-radius:4px;background:var(--sky)}

/* nav */
.nav{position:absolute;top:0;left:0;width:1200px;height:87px;background:var(--white)}
.nav-link{position:absolute;top:40px;font-size:12.5px;font-weight:700;color:var(--ink)}
.nav-phone{position:absolute;top:33px;left:777px;font-size:17px;font-weight:600;color:var(--ink);display:flex;align-items:center;gap:8px}

/* hero */
.hero{position:absolute;top:87px;left:0;width:1200px;height:638px;background:linear-gradient(135deg,#1560b8 0%,#1874cc 50%,#0f86d4 100%);overflow:hidden;color:var(--white);text-align:center}
.hero-skyline{position:absolute;left:0;bottom:0;width:1200px;height:230px;background:linear-gradient(180deg,rgba(255,255,255,0) 0%,rgba(255,255,255,.06) 100%)}
.hero-kicker{position:absolute;top:68px;width:100%;font-size:17px;letter-spacing:2px;font-weight:500}
.hero h1{position:absolute;top:104px;width:100%;font-size:46px;font-weight:500}
.hero h1 .hl{background:#2b8fe6;padding:0 14px;border-radius:6px}
.hero-copy{position:absolute;top:170px;left:265px;width:710px;font-size:15px;line-height:23px}
.hero-ask{position:absolute;top:283px;width:100%;font-size:16px;font-weight:600}

/* logos */
.partners{position:absolute;top:725px;left:0;width:1200px;height:107px;border-bottom:1px solid var(--line);display:flex;align-items:center;justify-content:space-between;padding:0 100px}
.partner{font-family:'Lexend',sans-serif;font-weight:500;font-size:21px;color:#2a2a2a;letter-spacing:1px}

/* about */
.about{position:absolute;top:832px;left:0;width:1200px;height:611px}
.about h2{position:absolute;top:92px;left:580px;font-size:37px;color:var(--navy)}
.about p{font-size:16px;line-height:23px;color:var(--ink)}

/* quote */
.quote{position:absolute;top:1443px;left:0;width:1200px;height:563px;background:var(--light)}
.quote h2{position:absolute;top:130px;left:114px;font-size:40px;color:var(--navy)}
.quote p{font-size:15px;line-height:22px}
.form-box{position:absolute;left:630px;top:49px;width:459px;height:416px;background:var(--green)}
.field{position:absolute;left:50px;width:362px;height:44px;background:var(--white);display:flex;align-items:center;gap:10px;padding-left:20px;font-size:13.5px;color:var(--muted)}
.field svg{width:14px;height:14px}

/* coverage */
.coverage{position:absolute;top:2006px;left:0;width:1200px;height:652px;background:linear-gradient(180deg,#143b8c 0%,#1a4596 70%,#21509f 100%);color:var(--white);text-align:center}
.coverage h2{position:absolute;top:90px;width:100%;font-size:31px;line-height:43px;font-weight:500}
.cov-sub{position:absolute;top:190px;width:100%;font-size:18px;font-weight:500}
.cov-card{position:absolute;width:153px;height:127px;background:var(--white);border-radius:4px;color:var(--navy);font-size:14px;font-weight:700}
.cov-card .box{position:absolute;left:10px;top:10px;width:18px;height:18px;border:1px solid #c7cfdd;background:#eef1f6}
.cov-card svg{position:absolute;left:46px;top:28px;width:62px;height:50px}
.cov-card span{position:absolute;left:0;right:0;top:94px;text-align:center}

/* agent */
.agent-bg{position:absolute;top:3167px;left:0;width:1200px;height:155px;background:var(--light)}
.agent-card{position:absolute;top:2743px;left:101px;width:988px;height:513px;background:var(--white);border:1px solid #c7d6ec;border-radius:4px}
.agent-card h2{position:absolute;left:539px;top:56px;font-size:35px;line-height:34px;color:var(--navy)}
.agent-label{position:absolute;left:546px;font-size:14px;color:var(--ink)}
.agent-input{position:absolute;left:542px;width:385px;height:47px;border:1px solid #9ab7e2;display:flex;align-items:center;gap:10px;padding-left:18px;font-size:13px;color:var(--muted)}

/* testimonials */
.testi{position:absolute;top:3320px;left:0;width:1200px;height:500px;text-align:center}
.testi h2{position:absolute;top:42px;width:100%;font-size:32px;color:var(--navy)}
.t-side{position:absolute;top:183px;width:250px;height:188px;background:var(--white);border:1px solid #e3e7ef;border-radius:8px;font-size:12px;color:var(--muted);line-height:17px;padding:45px 18px 0;overflow:hidden}
.t-main{position:absolute;left:311px;top:141px;width:588px;height:262px;background:var(--white);border:1px solid #b9cce8;border-radius:8px}
.avatar{position:absolute;border-radius:50%;background:#c9d3e0;border:3px solid #fff;box-shadow:0 2px 6px rgba(0,0,0,.15)}

/* cta */
.cta{position:absolute;top:3822px;left:0;width:1200px;height:143px;background:var(--green);color:var(--white)}

/* footer */
.footer{position:absolute;top:3965px;left:0;width:1200px;height:367px}
.f-col h4{font-size:14px;font-weight:700;color:var(--ink);letter-spacing:.3px}
.f-rule{width:146px;height:1px;background:var(--line);margin-top:8px;position:relative}
.f-rule:before{content:"";position:absolute;left:0;top:-1px;width:28px;height:3px;background:var(--green)}
.f-col ul{list-style:none;margin-top:12px}
.f-col li{font-size:12.5px;color:var(--ink);line-height:26.5px}
.social{width:24px;height:24px;border-radius:50%;background:var(--blue)}
</style>
</head>
<body>

<header class="nav">
  <span class="nav-link" style="left:112px">GET INSURANCE ⌄</span>
  <span class="nav-link" style="left:270px">PERSONAL ⌄</span>
  <span class="nav-link" style="left:397px">WHY US</span>
  <div class="brand abs" style="left:508px;top:21px">
    <div class="brand-mark"></div>
    <div class="brand-name">Halvern Crest<br>Insurance, LP</div>
  </div>
  <div class="nav-phone">
    <svg width="18" height="18" viewBox="0 0 24 24"><path fill="#7cb342" d="M6.6 10.8a15.1 15.1 0 0 0 6.6 6.6l2.2-2.2a1 1 0 0 1 1-.25 11.4 11.4 0 0 0 3.6.57 1 1 0 0 1 1 1V20a1 1 0 0 1-1 1A17 17 0 0 1 3 4a1 1 0 0 1 1-1h3.5a1 1 0 0 1 1 1c0 1.25.2 2.45.57 3.57a1 1 0 0 1-.25 1z"/></svg>
    (555) 013-0188
  </div>
  <div class="btn btn-green" style="left:963px;top:25px;width:142px;height:41px;font-size:12px">GET A QUOTE <svg class="chev" viewBox="0 0 8 12"><path d="M2 1l4 5-4 5" stroke="#fff" stroke-width="2" fill="none"/></svg></div>
</header>

<section class="hero">
  <div class="hero-skyline"></div>
  <div class="ph" role="img" aria-label="Smiling man in a denim shirt holding a laptop" style="left:50px;top:300px;width:362px;height:338px;background:linear-gradient(180deg,#3f7fc4 0%,#2f69ad 100%);border-radius:160px 160px 0 0;opacity:.85"></div>
  <div class="ph" role="img" aria-label="Smiling woman looking at her phone" style="left:857px;top:300px;width:303px;height:338px;background:linear-gradient(180deg,#d9e3ef 0%,#c3d2e4 100%);border-radius:150px 150px 0 0;opacity:.9"></div>
  <div class="hero-kicker">HALVERN CREST INSURANCE LP</div>
  <h1>Protecting What <span class="hl">Matters Most</span></h1>
  <p class="hero-copy">At Halvern Crest Insurance, we understand that your peace of mind is invaluable. Our mission is to protect what matters most to you—your home, your vehicle, your health, and your loved ones. With our comprehensive range of insurance solutions, we are dedicated to safeguarding your assets and providing you with the security you deserve.</p>
  <p class="hero-ask">For inquiries, please contact us at</p>
  <div class="btn btn-green" style="left:469px;top:330px;width:300px;height:49px;font-size:16px;font-weight:600">
    <svg width="18" height="18" viewBox="0 0 24 24"><path fill="#fff" d="M6.6 10.8a15.1 15.1 0 0 0 6.6 6.6l2.2-2.2a1 1 0 0 1 1-.25 11.4 11.4 0 0 0 3.6.57 1 1 0 0 1 1 1V20a1 1 0 0 1-1 1A17 17 0 0 1 3 4a1 1 0 0 1 1-1h3.5a1 1 0 0 1 1 1c0 1.25.2 2.45.57 3.57a1 1 0 0 1-.25 1z"/></svg>
    Call Us (555) 013-0188</div>
  <div class="btn btn-navy" style="left:469px;top:397px;width:300px;height:47px;font-size:14.5px;font-weight:600;background:#163b7e">
    <svg width="16" height="13" viewBox="0 0 16 13"><rect x="0" y="0" width="16" height="13" rx="1.5" fill="#fff"/><path d="M1 1l7 6 7-6" stroke="#163b7e" stroke-width="1.6" fill="none"/></svg>
    info@halverncrest.example</div>
</section>

<section class="partners" aria-label="Partner carriers">
  <span class="partner">DRAVO</span>
  <span class="partner">VELK</span>
  <span class="partner">Meridale Union</span>
  <span class="partner">Tarvix</span>
  <span class="partner">Brookwynd</span>
  <span class="partner">QZT</span>
  <span class="partner">Pellurian</span>
</section>

<section class="about">
  <div class="ph" style="left:101px;top:66px;width:437px;height:437px;border-radius:50%;border:2px solid #8fb8e6"></div>
  <div class="ph" role="img" aria-label="Family of four sitting together on a sofa making a roof with their hands" style="left:111px;top:76px;width:417px;height:417px;border-radius:50%;background:linear-gradient(160deg,#e7e3dc 0%,#cfc8bd 60%,#b9b2a8 100%)"></div>
  <div class="brand abs" style="left:79px;top:378px;width:257px;height:84px;background:#fff;border-radius:42px;box-shadow:0 4px 14px rgba(0,0,0,.12);padding-left:26px">
    <div class="brand-mark"></div>
    <div class="brand-name">Halvern Crest<br>Insurance, LP</div>
  </div>
  <div class="eyebrow abs" style="left:580px;top:70px">WHO WE ARE</div>
  <h2>Halvern Crest Insurance, LP</h2>
  <div class="underline" style="left:820px;top:142px;width:190px;height:3px"></div>
  <p class="abs" style="left:580px;top:164px;width:520px">Halvern Crest Insurance is a full-service, independent insurance agency with over three decades of experience in delivering comprehensive insurance solutions to individuals.</p>
  <div class="abs" style="left:580px;top:244px;width:2px;height:198px;background:var(--line)"></div>
  <p class="abs" style="left:595px;top:244px;width:520px">We proudly offer a diverse portfolio of products from more than 20 of the most reputable and financially secure companies in the industry. Our dedicated team of over 50 skilled professionals is committed to customizing these products and services to meet the unique needs of each client.</p>
  <p class="abs" style="left:595px;top:376px;width:520px">At Halvern Crest Insurance, our experts are focused on addressing the individual needs of our clients, ensuring exceptional service and support at every step</p>
  <div class="btn btn-green" style="left:571px;top:480px;width:173px;height:49px">GET A QUOTE <svg class="chev" viewBox="0 0 8 12"><path d="M2 1l4 5-4 5" stroke="#fff" stroke-width="2" fill="none"/></svg></div>
</section>

<section class="quote">
  <div class="eyebrow abs" style="left:114px;top:108px">CONTACT US</div>
  <h2>Get a Quote</h2>
  <div class="underline" style="left:245px;top:190px;width:125px;height:3px"></div>
  <p class="abs" style="left:114px;top:212px;width:470px">We believe that securing your home is one of the most important decisions you can make. Obtaining a comprehensive insurance quote is essential to understanding your coverage options and ensuring that your property is adequately protected against unforeseen events.</p>
  <p class="abs" style="left:114px;top:352px;width:480px">Our team of experienced professionals is here to guide you through the process, helping you find the right policy that meets your specific needs and budget. Don't leave your home's safety to chance—get a quote today and take the first step towards peace of mind.</p>
  <form class="form-box">
    <div class="field" style="top:40px"><svg viewBox="0 0 14 14"><circle cx="7" cy="4" r="3" fill="#9aa3b2"/><path d="M1 14a6 6 0 0 1 12 0z" fill="#9aa3b2"/></svg>Name</div>
    <div class="field" style="top:92px"><svg viewBox="0 0 14 14"><rect y="2" width="14" height="10" rx="1" fill="#9aa3b2"/><path d="M1 3l6 5 6-5" stroke="#fff" fill="none"/></svg>Email address</div>
    <div class="field" style="top:144px"><svg viewBox="0 0 24 24"><path fill="#9aa3b2" d="M6.6 10.8a15.1 15.1 0 0 0 6.6 6.6l2.2-2.2a1 1 0 0 1 1-.25 11.4 11.4 0 0 0 3.6.57 1 1 0 0 1 1 1V20a1 1 0 0 1-1 1A17 17 0 0 1 3 4a1 1 0 0 1 1-1h3.5a1 1 0 0 1 1 1c0 1.25.2 2.45.57 3.57a1 1 0 0 1-.25 1z"/></svg>Phone</div>
    <div class="field" style="top:196px"><svg viewBox="0 0 14 14"><path d="M7 0a5 5 0 0 1 5 5c0 4-5 9-5 9S2 9 2 5a5 5 0 0 1 5-5z" fill="#9aa3b2"/><circle cx="7" cy="5" r="2" fill="#fff"/></svg>Zip Code</div>
    <div class="field" style="top:252px;height:82px;align-items:flex-start;padding-top:14px"><svg viewBox="0 0 14 14"><ellipse cx="7" cy="6" rx="7" ry="5" fill="#9aa3b2"/><path d="M3 10l-1 4 4-3z" fill="#9aa3b2"/></svg>Message</div>
    <div class="btn btn-navy" style="left:50px;top:341px;width:190px;height:47px;font-size:13.5px">SEND MESSAGE <svg class="chev" viewBox="0 0 8 12"><path d="M2 1l4 5-4 5" stroke="#fff" stroke-width="2" fill="none"/></svg></div>
  </form>
  <svg class="abs" style="left:600px;top:510px" width="100" height="100" viewBox="0 0 100 100"><path d="M90 0v16c0 8-6 10-14 10H24c-8 0-14 4-14 12v62" stroke="#2a7bd0" stroke-width="1.6" stroke-dasharray="4 4" fill="none"/></svg>
</section>

<section class="coverage">
  <h2>Now more Specifically, what type of<br>Personal Protection are you looking for?</h2>
  <div class="underline" style="left:762px;top:176px;width:130px;height:3px;background:#4aa7ef"></div>
  <div class="cov-sub">Select up to three coverages</div>

  <div class="cov-card" style="left:249px;top:240px"><div class="box"></div><svg viewBox="0 0 62 50" fill="none" stroke="#2a6bc4" stroke-width="2"><path d="M6 32h50v-8l-8-3-8-8H20l-8 8-6 3z"/><circle cx="18" cy="33" r="5"/><circle cx="44" cy="33" r="5"/></svg><span>Auto</span></div>
  <div class="cov-card" style="left:434px;top:240px"><div class="box"></div><svg viewBox="0 0 62 50" fill="none" stroke="#2a6bc4" stroke-width="2"><path d="M14 22L31 8l17 14M18 20v22h26V20"/><rect x="27" y="30" width="8" height="12"/></svg><span>Home</span></div>
  <div class="cov-card" style="left:619px;top:240px"><div class="box"></div><svg viewBox="0 0 62 50" fill="none" stroke="#2a6bc4" stroke-width="2"><circle cx="38" cy="14" r="8"/><path d="M33 20L18 40M22 35l5 4M25 31l4 3"/></svg><span>Renters</span></div>
  <div class="cov-card" style="left:804px;top:240px"><div class="box"></div><svg viewBox="0 0 62 50" fill="none" stroke="#2a6bc4" stroke-width="2"><rect x="16" y="8" width="30" height="36"/><path d="M22 14h4M30 14h4M38 14h2M22 22h4M30 22h4M38 22h2M22 30h4M30 30h4M38 30h2"/></svg><span>Condo</span></div>

  <div class="cov-card" style="left:249px;top:390px"><div class="box"></div><svg viewBox="0 0 62 50" fill="none" stroke="#2a6bc4" stroke-width="2"><path d="M12 22a19 12 0 0 1 38 0zM31 22v20"/><circle cx="20" cy="34" r="3"/><circle cx="42" cy="34" r="3"/></svg><span>Umbrella</span></div>
  <div class="cov-card" style="left:434px;top:390px"><div class="box"></div><svg viewBox="0 0 62 50" fill="none" stroke="#2a6bc4" stroke-width="2"><path d="M8 16h44v24H8zM8 16l6-6h38"/><rect x="16" y="24" width="10" height="16"/><rect x="32" y="24" width="12" height="8"/></svg><span>Mobile Home</span></div>
  <div class="cov-card" style="left:619px;top:390px"><div class="box"></div><svg viewBox="0 0 62 50" fill="none" stroke="#2a6bc4" stroke-width="2"><path d="M6 36V14h36l10 10v12z"/><circle cx="16" cy="38" r="4"/><circle cx="42" cy="38" r="4"/><rect x="12" y="20" width="10" height="8"/></svg><span>Motor Home</span></div>
  <div class="cov-card" style="left:804px;top:390px"><div class="box"></div><svg viewBox="0 0 62 50" fill="none" stroke="#2a6bc4" stroke-width="2"><circle cx="15" cy="34" r="8"/><circle cx="47" cy="34" r="8"/><path d="M15 34l10-14h12l10 14M30 20l-2-6"/></svg><span>ATV</span></div>

  <div class="btn btn-green" style="left:511px;top:549px;width:171px;height:47px;font-size:12.5px">SHOW MORE <svg class="chev" viewBox="0 0 8 12"><path d="M2 1l4 5-4 5" stroke="#fff" stroke-width="2" fill="none"/></svg></div>
</section>

<div class="agent-bg"></div>
<section class="agent-card">
  <div class="ph" role="img" aria-label="Smiling woman in glasses pointing toward the form" style="left:52px;top:40px;width:403px;height:417px;border-radius:24px;background:linear-gradient(160deg,#2d7bd0 0%,#1e68bc 100%)"></div>
  <h2>Find &nbsp;the right local<br>Agent for you</h2>
  <div class="underline" style="left:539px;top:128px;width:130px;height:3px"></div>
  <p class="abs" style="left:539px;top:156px;width:400px;font-size:13px;line-height:19px;color:var(--navy)">Just some basic information. The address of your personal property will help in finding the right local agent for you.</p>
  <div class="agent-label" style="top:216px">Enter the address of your insurable property</div>
  <div class="agent-input" style="top:243px"><svg width="15" height="12" viewBox="0 0 14 12"><rect width="14" height="11" rx="1" fill="#9ab7e2"/><path d="M1 1l6 5 6-5" stroke="#fff" fill="none"/></svg>Email address</div>
  <div class="agent-label" style="top:318px">Zip code (require)</div>
  <div class="agent-input" style="top:338px"><svg width="12" height="15" viewBox="0 0 14 14"><path d="M7 0a5 5 0 0 1 5 5c0 4-5 9-5 9S2 9 2 5a5 5 0 0 1 5-5z" fill="#9ab7e2"/></svg>Type Zip code</div>
  <div class="btn btn-green" style="left:538px;top:407px;width:173px;height:49px;font-size:14px">NEXT STEP <svg class="chev" viewBox="0 0 8 12"><path d="M2 1l4 5-4 5" stroke="#fff" stroke-width="2" fill="none"/></svg></div>
  <svg class="abs" style="left:400px;top:410px" width="140" height="90" viewBox="0 0 140 90"><path d="M60 10c10 10-4 28-10 18s20 40 78 20" stroke="#2a6bc4" stroke-width="1.3" stroke-dasharray="3 3" fill="none"/></svg>
</section>

<section class="testi">
  <div class="eyebrow abs" style="width:100%;top:18px">TESTIMONIALS</div>
  <h2>What Our Client Says about us</h2>
  <div class="underline" style="left:708px;top:96px;width:140px;height:3px"></div>
  <div class="t-side" style="left:190px;padding-right:130px">"As a CPA, I find this team especially helpful; they guide me to the best plans."</div>
  <div class="t-side" style="left:760px;padding-left:150px">"Easy to navigate. Fast help every time."</div>
  <div class="avatar" role="img" aria-label="Client portrait" style="left:235px;top:104px;width:42px;height:42px"></div>
  <div class="avatar" role="img" aria-label="Client portrait" style="left:200px;top:364px;width:32px;height:32px"></div>
  <div class="avatar" role="img" aria-label="Client portrait" style="left:990px;top:97px;width:28px;height:28px"></div>
  <div class="avatar" role="img" aria-label="Client portrait" style="left:1016px;top:384px;width:40px;height:40px"></div>
  <svg class="abs" style="left:130px;top:247px" width="24" height="40" viewBox="0 0 24 40"><path d="M20 2L4 20l16 18" stroke="#1976d2" stroke-width="3" fill="none"/></svg>
  <svg class="abs" style="left:1044px;top:247px" width="24" height="40" viewBox="0 0 24 40"><path d="M4 2l16 18L4 38" stroke="#1976d2" stroke-width="3" fill="none"/></svg>
  <div class="t-main">
    <svg class="abs" style="left:273px;top:38px" width="46" height="32" viewBox="0 0 46 32"><path d="M2 0h18v18l-8 14H4l6-14H2zM26 0h18v18l-8 14h-8l6-14h-8z" fill="#1976d2"/></svg>
    <p class="abs" style="left:60px;top:80px;width:468px;font-size:15.5px;line-height:22px;color:var(--navy);font-weight:500">"Lorem ipsum dolor sit amet, consectetur adipiscing elit, sed do eiusmod tempor incididunt ut labore et dolore magna aliqua. Ut enim ad minim veniam, quis nostrud exercitation ullamco laboris n"</p>
    <div class="abs" style="width:100%;top:190px;font-size:15px;font-weight:600;color:var(--ink)">Dara Willet</div>
    <div class="abs" style="width:100%;top:210px;font-size:17px;color:#f2b71f;letter-spacing:2px">★★★★★</div>
  </div>
</section>

<section class="cta">
  <div class="abs" style="left:160px;top:50px;width:44px;height:44px;border:3px solid #fff;border-radius:4px"></div>
  <h3 class="abs" style="left:232px;top:44px;font-size:25px">Get Started with Halvern Crest Insurance</h3>
  <p class="abs" style="left:232px;top:86px;font-size:14px">Lorem ipsum dolor sit amet, consectetur adipiscin</p>
  <div class="btn" style="left:862px;top:52px;width:255px;height:52px;background:#fff;color:var(--blue);font-size:17px">Try For FREE →</div>
</section>

<footer class="footer">
  <div class="brand abs" style="left:151px;top:42px">
    <div class="brand-mark" style="width:36px;height:36px"></div>
    <div class="brand-name" style="font-size:19px;line-height:22px">Halvern Crest<br>Insurance, LP</div>
  </div>
  <p class="abs" style="left:155px;top:120px;width:230px;font-size:10.5px;line-height:14px;color:var(--muted)">Lorem ipsum dolor sit amet, consectetur adipiscing elit, sed do eiusmod tempor incididunt ut labore et dolore</p>
  <div class="abs" style="left:159px;top:186px;display:flex;gap:22px" aria-label="Social links">
    <div class="social" role="img" aria-label="Social profile"></div>
    <div class="social" role="img" aria-label="Social profile"></div>
    <div class="social" role="img" aria-label="Social profile"></div>
  </div>
  <div class="f-col abs" style="left:435px;top:55px"><h4>NAVIGATION</h4><div class="f-rule"></div>
    <ul><li>Home</li><li>About Us</li><li>Insurance</li><li>Services</li><li>Testimonials</li></ul></div>
  <div class="f-col abs" style="left:653px;top:52px"><h4>INSURANCE</h4><div class="f-rule"></div>
    <ul><li>Auto Insurance</li><li>Home Insurance</li><li>Life Insurance</li><li>Car Insurance</li><li>Business Insurance</li></ul></div>
  <div class="f-col abs" style="left:877px;top:55px"><h4>CONTACT US</h4><div class="f-rule"></div></div>
  <svg class="abs" style="left:877px;top:108px" width="16" height="16" viewBox="0 0 24 24"><path fill="#1976d2" d="M6.6 10.8a15.1 15.1 0 0 0 6.6 6.6l2.2-2.2a1 1 0 0 1 1-.25 11.4 11.4 0 0 0 3.6.57 1 1 0 0 1 1 1V20a1 1 0 0 1-1 1A17 17 0 0 1 3 4a1 1 0 0 1 1-1h3.5a1 1 0 0 1 1 1c0 1.25.2 2.45.57 3.57a1 1 0 0 1-.25 1z"/></svg>
  <p class="abs" style="left:906px;top:104px;font-size:12.5px;line-height:21px">Phone Number<br>(555) 013-0188</p>
  <svg class="abs" style="left:877px;top:170px" width="16" height="13" viewBox="0 0 14 12"><rect width="14" height="11" rx="1" fill="#1976d2"/><path d="M1 1l6 5 6-5" stroke="#fff" fill="none"/></svg>
  <p class="abs" style="left:906px;top:160px;font-size:12.5px;line-height:21px">Email address<br>info@halverncrest.example</p>
  <div class="abs" style="left:0;top:297px;width:1200px;height:1px;background:var(--line)"></div>
  <p class="abs" style="left:160px;top:326px;font-size:10.5px;color:var(--muted)">© 2025 Halvern Crest Insurance, LP. All Rights Reserved</p>
  <p class="abs" style="left:902px;top:326px;font-size:10.5px;color:var(--muted);word-spacing:4px">Terms of use &nbsp;Privacy Policy &nbsp;Sitemap</p>
</footer>

</body>
</html>
```